One label design for 3 different sizes of honey bottles

Our honey company -- Amber Hollow Apiary -- needs new product labels, integrating our new name and logo. We would like one label design that presents equally well on three different sizes of plastic honey bottles. Designs should include a front and back label.

Keep in mind that we really like our old label. Please submit designs that have a similar color and font scheme as the old label.

In the uploaded files, you will find (1) detailed content instructions for each size label (2 lb, 1 lb, 8 oz), (2) photo of three plastic bottles without labels, (3) *.ai file for the new company logo, and (4) image of old package label.

Requirements
Must have
• Same look and feel as our old label, but with our new name and logo

```html
<!DOCTYPE html>
<html lang="en">
<head>
<meta charset="utf-8">
<title>Amber Hollow Apiary – Honey Label</title>
<link rel="stylesheet" href="https://fonts.googleapis.com/css2?family=Rye&family=Courier+Prime:wght@400;700&display=swap">
<style>
  :root {
    --canvas: #ffffff;
    --label-cream: #e9e4d9;
    --label-cream-light: #f1ede4;
    --label-edge: #f6f3ec;
    --ink: #2f302c;
    --ink-soft: #3d3e39;
    --art-tone: #d3ccbe;
    --art-tone-deep: #bfb7a6;
  }
  html, body {
    margin: 0;
    padding: 0;
    width: 1200px;
    height: 1200px;
    overflow: hidden;
    background: var(--canvas);
  }
  .canvas {
    position: relative;
    width: 1200px;
    height: 1200px;
  }
  .front-label {
    position: absolute;
    left: 205px;
    top: 60px;
    width: 790px;
    height: 1080px;
  }
  .label-tagline {
    font-family: "Courier Prime", monospace;
    font-weight: 700;
    font-size: 34px;
    letter-spacing: 2px;
    fill: var(--label-cream-light);
  }
  .label-title {
    font-family: "Rye", serif;
    font-size: 168px;
    fill: var(--ink);
  }
  .brand-name {
    font-family: "Courier Prime", monospace;
    font-weight: 700;
    font-size: 44px;
    fill: var(--ink);
  }
  .net-weight {
    font-family: "Courier Prime", monospace;
    font-weight: 700;
    font-size: 23px;
    fill: var(--ink);
  }
</style>
</head>
<body>
<main class="canvas">
  <svg class="front-label" viewBox="0 0 790 1080" xmlns="http://www.w3.org/2000/svg" aria-label="Front label: Local, Pure, Raw Honey by Amber Hollow Apiary">
    <defs>
      <linearGradient id="label-paper" x1="0" y1="0" x2="1" y2="0">
        <stop offset="0" stop-color="#e3ded2"/>
        <stop offset="0.5" stop-color="#ece8de"/>
        <stop offset="1" stop-color="#e3ded2"/>
      </linearGradient>
      <radialGradient id="art-fill" cx="0.5" cy="0.5" r="0.6">
        <stop offset="0" stop-color="var(--art-tone)"/>
        <stop offset="1" stop-color="var(--label-cream)" stop-opacity="0"/>
      </radialGradient>
      <path id="tagline-curve" d="M120 205 Q395 150 670 205"/>
    </defs>

    <!-- label body -->
    <path class="label-outer" d="M0 112 L30 82 Q395 -14 760 82 L790 112 V1040 Q790 1080 750 1080 H40 Q0 1080 0 1040 Z"
          fill="var(--label-edge)"/>
    <path class="label-panel" d="M14 118 L40 94 Q395 4 750 94 L776 118 V1036 Q776 1066 746 1066 H44 Q14 1066 14 1036 Z"
          fill="url(#label-paper)"/>
    <path class="label-frame" d="M32 126 L54 108 Q395 24 736 108 L758 126 V1028 Q758 1048 738 1048 H52 Q32 1048 32 1028 Z"
          fill="none" stroke="var(--ink)" stroke-width="4"/>

    <!-- tagline ribbon -->
    <path class="tagline-ribbon" d="M100 190 Q395 132 690 190 L690 240 Q395 182 100 240 Z" fill="var(--ink)"/>
    <circle cx="100" cy="215" r="9" fill="var(--ink)"/>
    <circle cx="690" cy="215" r="9" fill="var(--ink)"/>
    <text class="label-tagline" text-anchor="middle" dy="14">
      <textPath href="#tagline-curve" startOffset="50%">LOCAL • PURE • RAW</textPath>
    </text>

    <!-- title -->
    <text class="label-title" x="395" y="450" text-anchor="middle" textLength="610" lengthAdjust="spacingAndGlyphs">HONEY</text>

    <!-- illustration area -->
    <rect class="label-artwork" x="90" y="500" width="610" height="400" rx="30"
          fill="url(#art-fill)" role="img"
          aria-label="Illustration: faint large honeybee and state outline with a small bee, river and pine trees"/>

    <!-- brand name -->
    <text class="brand-name" x="395" y="770" text-anchor="middle">Amber Hollow Apiary</text>

    <!-- corner flourishes -->
    <rect class="corner-flourish" x="56" y="905" width="120" height="120" rx="12"
          fill="var(--art-tone-deep)" opacity="0.35" role="img" aria-label="Decorative corner flourish"/>
    <rect class="corner-flourish" x="614" y="905" width="120" height="120" rx="12"
          fill="var(--art-tone-deep)" opacity="0.35" role="img" aria-label="Decorative corner flourish"/>

    <!-- net weight -->
    <text class="net-weight" x="395" y="990" text-anchor="middle">Net Wt. 2 LB (907 g)</text>
    <g class="net-weight-rule" fill="var(--ink)" stroke="var(--ink)">
      <line x1="220" y1="1018" x2="570" y2="1018" stroke-width="2"/>
      <path d="M210 1018 L222 1012 L222 1024 Z" stroke="none"/>
      <path d="M580 1018 L568 1012 L568 1024 Z" stroke="none"/>
      <path d="M395 1011 L402 1018 L395 1025 L388 1018 Z" stroke="none"/>
    </g>
  </svg>
</main>
</body>
</html>
```